Flyer-Design für Betreuer von Altenwohn- und Pflegeheimen
Zielgruppe
Die vaxo-pro GmbH betreut Altenwohn- und Pflegeheime im Bereich Arbeitsschutz.
Die Bereiche sind:
- Beratung & Schulung für Arbeitssicherheit, Erste Hilfe und Brandschutz
- Prüfung von Arbeitsmitteln und Medizingeräten
- Reparatur& Wartung von Elektrogeräten
- ein Partner für die 'Lösung aus einer Hand'
Die Zielgruppe sind die Betreiber (Inhaber) und Leitungen von Pflegeeinrichtungen für ältere Menschen und MEnschen mit Behidnerungen
Aufgabenstellung
Das Format soll quadratisch analog dem Logo der vaxo-pro GmbH mit einer Seitenlänge von 210mm sein (Breite DIN A4). Der Folder soll einmal gefaltet sein..
Das Logo beschreibt die Leistungen der vaxo-pro
- linkes oberes Quadrat = 'Beratung&Schulung'
- rechtes oberes Quadrat = 'Prüfung'
- linkes unteres Quadrat = 'Reparatur & Wartung'
- rechtes unteres Quadrat mit dem Haken = 'ein Partner ('...alles aus einer Hand!' <-- wobei mir persönlich diese Wortwahl nicht gefällt')
Der Folder soll auf der ersten Seite beim Leser das Gefühl wecken: 'Das MUSS ich lesen...' <-- Neugierde wecken.
Die beiden Innenseiten sollen die jeweiligen Quadrate der Leistungen beschreiben (siehe oben)
Die Rückseite enthält Angaben zu Referenzen und die Kontaktdaten.
Die Referenzen sollen 'allgemein' gehalten werden:
• kommunale Betreiber
• gemeinnützige Betreiber mit vielen Einrichtungen in ganz Bayern
• viele kleine Einrichtungen mit wenigen Betten ebenso wie
• private große Betreiber mit 1500 Pflegeplätzen und mehr
Karte mit Bullets von Bayern (siehe hochgeladene Datei) - vorerst dieses Bild, in der finalen Version soll diese Karte nicht so sehr nach Plurimo aussehen.
Weieter habe jetzt noch Texte als Word-Datei hinzugefügt...

```html
<!DOCTYPE html>
<html lang="de">
<head>
<meta charset="utf-8">
<title>vaxo-pro Folder</title>
<link rel="stylesheet" href="https://fonts.googleapis.com/css2?family=Raleway:wght@300;400;500;700;800&display=swap">
<style>
:root{
  --stage:#434345;
  --yellow:#fcc400;
  --white:#ffffff;
  --panel:#ebebeb;
  --dark-panel:#6d6d6d;
  --ink:#3a3a3a;
  --muted:#555555;
  --logo-grey:#8a8a8a;
}
*{box-sizing:border-box;margin:0;padding:0}
html,body{width:1200px;height:1200px;overflow:hidden;background:var(--stage)}
body{font-family:"Raleway",sans-serif;color:var(--ink);position:relative}
.abs{position:absolute}
.spread{position:absolute;left:58px;width:1092px;background:var(--white);overflow:hidden}
.spread--outside{top:35px;height:546px}
.spread--inside{top:606px;height:546px}

/* outside: back page */
.back{left:0;top:0;width:546px;height:546px;background:var(--yellow)}
.map{left:14px;top:0;width:532px;height:478px;border-radius:0 0 120px 90px;
  background:radial-gradient(ellipse at 50% 55%,#ffffff 0%,#ffffff 62%,#fde9a3 82%,var(--yellow) 100%)}
.refs{left:52px;top:0;width:194px;height:167px;background:var(--panel);padding:30px 14px 0 27px}
.refs h2{font-weight:400;font-size:18px;margin-bottom:12px;color:#222}
.refs li{font-size:7px;line-height:11px;margin-bottom:11px}
.contact{left:216px;top:490px;display:flex;gap:9px;font-size:7px;line-height:11px;color:#222}
.contact b{font-weight:700}

/* outside: cover */
.cover{left:546px;top:0;width:546px;height:546px;
  background:radial-gradient(ellipse at 50% 70%,#ffffff 0%,#f6f6f6 45%,#d9d9d9 100%)}
.claim{left:164px;top:100px;display:flex;gap:18px;font-weight:400;font-size:18px;letter-spacing:.5px;color:#777}
.cube{left:144px;top:145px;width:252px;height:260px;
  background:linear-gradient(150deg,#ffe36a 0%,#fcc400 45%,#d59b00 100%);border-radius:4px}
.brand{display:flex;align-items:center;gap:8px;color:var(--logo-grey);font-weight:500}
.brand::before{content:"";width:.72em;height:.72em;background:var(--yellow)}
.cover .brand{position:absolute;left:196px;top:455px;font-size:35px}

/* lists */
ul{list-style:none}
li{position:relative;padding-left:12px}
li::before{content:"";position:absolute;left:0;top:2px;width:5px;height:5px;background:var(--yellow)}
.caps{font-weight:800;text-transform:uppercase}

/* inside */
.partner{left:0;top:30px;width:224px;height:234px;background:var(--yellow);padding:22px 10px 0 41px}
.section-title{font-weight:400;font-size:18px;color:#222;white-space:nowrap}
.partner .section-title{margin-bottom:9px}
.partner p{font-size:7px;line-height:11px;font-weight:800;text-transform:uppercase;color:#222;margin-bottom:11px}
.fig-partner{left:66px;top:302px;width:216px;height:136px;border-radius:8px;
  background:linear-gradient(90deg,#f1f1f1 0%,#f1f1f1 40%,#fde07a 100%)}
.inside-brand{left:318px;top:96px;font-size:40px}

.benefits{left:306px;top:156px;width:212px;height:390px;background:var(--dark-panel);padding:20px 22px 0 12px;color:#e8e8e8}
.benefits h3{font-weight:400;font-size:18px;color:var(--yellow);margin:0 0 8px 14px}
.benefits li{font-size:6.6px;line-height:11px;margin-bottom:11px}
.benefits li::before{top:3px}
.benefits b{font-weight:800;text-transform:uppercase;color:#fff}

.service{font-size:6.6px;line-height:11px;color:var(--muted)}
.service li{margin-bottom:11px}
.service b{display:block;font-weight:800;text-transform:uppercase;color:#222}

.check-box{left:762px;top:0;width:176px;height:108px;background:var(--panel)}
.check-title{left:736px;top:30px}
.check-list{left:1012px;top:74px;width:270px}
.check-list{left:1012px}
.fig-check{left:958px;top:26px;width:112px;height:80px;border-radius:6px;background:linear-gradient(90deg,#efefef,#fde07a)}
.fig-team{left:578px;top:78px;width:160px;height:164px;border-radius:8px;background:linear-gradient(180deg,#f2f2f2,#e2e2e2)}

.advice-box{left:570px;top:255px;width:202px;height:203px;background:var(--panel);padding:26px 12px 0 22px}
.advice-box .section-title{margin-bottom:10px}

.repair-box{left:888px;top:298px;width:204px;height:226px;background:var(--panel);padding:46px 12px 0 20px}
.repair-title{left:856px;top:316px}
.repair-box li{font-size:6.6px;line-height:10px;color:var(--muted);margin-bottom:12px}
.fig-repair{left:798px;top:382px;width:80px;height:92px;border-radius:6px;background:linear-gradient(180deg,#fde07a,#efefef)}
</style>
</head>
<body>

<section class="spread spread--outside">
  <div class="abs back">
    <div class="abs map" role="img" aria-label="Karte von Bayern mit Markierungen der betreuten Einrichtungen rund um München, Augsburg, Ingolstadt, Regensburg, Passau, Rosenheim und Ulm, dazu eine jubelnde Strichfigur mit Stern"></div>
    <div class="abs refs">
      <h2>Referenzen</h2>
      <ul>
        <li>kommunale Betreiber</li>
        <li>gemeinnützige Betreiber mit vielen<br>Einrichtungen in ganz Bayern</li>
        <li>viele kleine Einrichtungen mit wenigen<br>Betten ebenso wie private große Betreiber<br>mit 1.500 Pflegeplätzen und mehr</li>
      </ul>
    </div>
    <div class="abs contact">
      <div><b>vaxo-pro GmbH</b><br>Lindenweg 14<br>85600 Musterfeld</div>
      <div>+49 (0) 8100 55510-0<br>info@vaxo-pro.de<br>www.vaxo-pro.de</div>
    </div>
  </div>
  <div class="abs cover">
    <div class="abs claim"><span>VIELSEITIG</span><span>PRÄZISE</span><span>KOMPAKT</span></div>
    <div class="abs cube" role="img" aria-label="Gelber glänzender Würfel mit weichem Schatten"></div>
    <div class="brand">vaxo-pro</div>
  </div>
</section>

<section class="spread spread--inside">
  <div class="abs partner">
    <h2 class="section-title">Ein Partner – ganzer Service</h2>
    <p>Koordination aller Termine<br>und Fälligkeiten</p>
    <p>Reibungslose Prüfabläufe<br>ohne wesentlicher Störung<br>des Tagesgeschäftes</p>
    <p>Wirtschaftliche Mängelbeseitigung</p>
    <p>Inventarisierung durch ein<br>eigenes Kennzeichnungs- und<br>Dokumentationssystem</p>
    <p>vaxo-online - aktuelle Informationen<br>und Dokumentationen online auf<br>einen Klick</p>
  </div>
  <div class="abs fig-partner" role="img" aria-label="Strichfigur mit Stift neben einem großen gelben Haken"></div>

  <div class="abs brand inside-brand">vaxo-pro</div>

  <div class="abs benefits">
    <h3>Ihre Vorteile</h3>
    <ul>
      <li><b>Mehr Sicherheit für Mitarbeiter und Bewohner</b> durch geschulten Umgang der Mitarbeiter mit Ihren Medizingeräten</li>
      <li><b>Minimierung der Unfallgefahr</b> und Gewährleistung der Sicherheit Ihrer Mitarbeiter und Bewohner</li>
      <li><b>Detaillierter Überblick</b> zum Ist-Zustand Ihrer technischen Geräte und Anlagen</li>
      <li><b>Steigerung Ihrer Betriebssicherheit</b> durch optimales Erfüllen gesetzlicher, berufsgenossenschaftlicher und versicherungstechnischer Vorgaben</li>
      <li><b>Kostensenkung</b> durch geringere Ausfallzeiten und längere Lebensdauer der Geräte</li>
      <li><b>Erhöhung Ihrer Wirtschaftlichkeit</b> durch klare Zuständigkeiten und straff organisierte, effiziente Prozessabläufe</li>
      <li><b>Kompetente Unterstützung und Hilfe</b> zu vielen Themen und Fragen rund um Ihre Pflegeeinrichtung</li>
      <li><b>Effizienzte und effektive Abwicklung</b> mit einem einzigen Partner für alle Belange</li>
    </ul>
  </div>

  <div class="abs fig-team" role="img" aria-label="Strichfigur an einer Tafel vor einer Gruppe von Zuhörern"></div>

  <div class="abs check-box"></div>
  <h2 class="abs section-title check-title">Prüfung &amp; Inspektion</h2>
  <div class="abs fig-check" role="img" aria-label="Strichfigur mit Stift und Checkliste"></div>
  <ul class="abs service check-list" style="left:812px;top:74px;width:210px">
    <li><b>Technische Geräte</b>sicherheitstechnische<br>Überprüfung der aktiven<br>Medizinprodukte / Hilfsmittel</li>
    <li><b>Elektronische Geräte</b>Prüfung der elektrischen Betriebsmittel (Haus- und Küchengeräte, Werkzeuge, bewohnereigene Geräte)</li>
    <li><b>Elektrische Anlagen</b>Prüfung der gesamten elektrischen Anlage inklusive Thermografie (Wärmbildkamera)</li>
    <li><b>Inventarisierung</b>Erstellung eines Bestandsverzeichnisses</li>
    <li><b>Dokumentation</b>Mängelliste und Angebot zur Behebung</li>
  </ul>

  <div class="abs advice-box">
    <h2 class="section-title">Beratung &amp; Schulung</h2>
    <ul class="service">
      <li><b>Bedienung</b>Schulung der Mitarbeiter im Umgang mit aktiven Medizinprodukten / Hilfsmitteln</li>
      <li><b>Optimierung</b>Unterstützung bei Themen zum Qualitätsmanagement und zur Prozessgestaltung</li>
      <li><b>Sicherheit</b>Betreuung als externe Fachkraft für Arbeitssicherheit und Brandschutz</li>
    </ul>
  </div>

  <div class="abs repair-box">
    <ul>
      <li>herstellerunabhängiger Service für<br>Medizinprodukte / Hilfsmittel, wie z. B.</li>
      <li>Pflegebetten</li>
      <li>Steckbeckenspülen mit Nachweis<br>der Desinfektionsleitung</li>
      <li>Decken-/Tuch-/Sitzlifter / Aufstehhilfen</li>
      <li>Pflegebadewannen</li>
      <li>Sauerstoffkonzentratoren</li>
      <li>diverse weitere Geräte</li>
    </ul>
  </div>
  <h2 class="abs section-title repair-title">Reparatur &amp; Wartung</h2>
  <div class="abs fig-repair" role="img" aria-label="Strichfigur mit großem gelben Schraubenschlüssel"></div>
</section>

</body>
</html>
```